Compelling Home Page for Clip Harbor Partners

We are a Video SEO specialist that get websites on top of the front page of Zentrova and FlickBarn with video thumbprints that generate great traffic. Video SEO is all we do

see what we're offering at a salespage www.plumfieldreels.example. However, please omit "guarantee"

he home page should introduce our company as a premier company for helping brands get their videos on the front page of zentrova and high up in flickbarn. Should incorporate video "thumbnails" as part of the design. These could be the "triangular click buttons" or little video screens you see as "thumbnails" Needs a prominent place for a video about videoSEO. on Left side of page towards the top.

Needs buttons across the top for other pages. See www.brastonclips.example for frame of reference we want to be better than them.

Must incorporate our logo. We'd like to see the logo on dark background as well as white background.

Simple but with bright and vibrant highlights that look sophisticated, cutting edge and accountable. Shows credentials. Links with examples of thumbnails that are on the front page

We want to beat www.brastonclips.example check it out for point of reference

Target Market(s)

large corporations who have videos already and want to get better traction. Marlow 500. Advertising Agencies for Marlow 500's

Requirements
Must have
• Incorporate our logo. clean, easy to read

```html
<!DOCTYPE html>
<html lang="en">
<head>
<meta charset="utf-8">
<title>Clip Harbor Partners – Video SEO</title>
<link href="https://fonts.googleapis.com/css2?family=Ubuntu:wght@400;500;700&family=Open+Sans:wght@400;700&display=swap" rel="stylesheet">
<style>
:root{
  --ink:#1b1f23;
  --dark:#1e2226;
  --text:#222;
  --muted:#666;
  --red:#c8141c;
  --orange:#f6a800;
  --yellow:#f3c21a;
  --green:#6cc12a;
  --green-dark:#2f8f1a;
  --blue:#1a9ad8;
  --blue-dark:#1c5fa8;
  --line:#d8dde2;
  --panel:#eef3f8;
}
*{box-sizing:border-box;margin:0;padding:0}
html,body{width:1200px;height:1048px;overflow:hidden}
body{position:relative;background:linear-gradient(#e9ecef 560px,#f2f3f4 700px,#fff 900px);font-family:"Ubuntu",sans-serif;color:var(--text)}
a{color:inherit;text-decoration:none}

.topbar{position:absolute;left:0;top:0;width:1200px;height:78px;background:var(--dark)}
.brand{position:absolute;display:flex;align-items:center;gap:12px;font-family:"Ubuntu",sans-serif;font-weight:400;color:#e9ecef;font-size:35px;letter-spacing:-.3px}
.brand-dot{width:44px;height:44px;border-radius:50%;background:var(--blue)}
.topbar .brand{left:143px;top:15px}
.tagline{position:absolute;left:564px;top:28px;font-family:"Open Sans",sans-serif;font-size:12px;line-height:15px;color:#e6e6e6}
.tagline .hl-y{color:var(--yellow)}
.tagline .hl-g{color:var(--green)}

.stage{position:absolute;left:113px;top:78px;width:975px;height:582px;background:#fff;box-shadow:0 4px 14px rgba(0,0,0,.15)}
.navbar{position:absolute;left:0;top:0;width:975px;height:65px;background:linear-gradient(90deg,#dcebf5,#eef5fa 50%,#dcebf5);border-bottom:1px solid #c8d6e0}
.nav{position:absolute;left:21px;top:17px;display:flex;gap:11px;list-style:none}
.nav a{display:flex;align-items:center;gap:7px;height:30px;padding:0 9px 0 7px;border-radius:15px;background:rgba(255,255,255,.55);box-shadow:inset 0 0 0 1px rgba(0,0,0,.06);font-weight:700;font-size:15px;color:#222}
.nav a .pi{width:15px;height:15px}
.nav a.is-active{background:linear-gradient(#3cb7f0,#1688cc);color:#fff}
.price{position:absolute;right:28px;top:14px;display:flex;gap:10px;align-items:flex-start}
.price-icon{width:62px;height:52px}
.price-label{font-size:14px;font-weight:500;line-height:15px;color:#222}
.price-label strong{display:block;font-size:24px;color:var(--red);line-height:28px}

.hero{position:absolute;left:0;top:65px;width:975px;height:400px;background:radial-gradient(ellipse at 70% 40%,#fbfdff,#e4edf5 70%,#d9e4ee)}
.monitor{position:absolute;left:39px;top:45px;width:422px;height:316px}
.screen{position:absolute;left:9px;top:9px;width:404px;height:242px;background:linear-gradient(135deg,#f4f6f9,#dfe5ec 60%,#cfd6de)}
.screen-copy{position:absolute;left:32px;top:130px;font-weight:700;color:#111}
.screen-copy .big{font-size:20px}
.screen-copy .big span{color:var(--red);font-weight:500}
.screen-copy .think{font-size:40px;font-style:italic;font-weight:400;line-height:38px;margin-left:22px}
.screen-copy .small{font-size:12px;margin-top:2px}
.screen-copy .small span{color:var(--red)}
.play-big{position:absolute;left:176px;top:94px;width:60px;height:64px}
.hero-copy{position:absolute;left:483px;top:60px;width:440px;font-family:"Open Sans",sans-serif;font-size:15px;line-height:20px;color:#222}
.hero-copy strong{font-weight:700}
.hero-copy .reasons{color:var(--red)}
.btn{position:absolute;display:flex;align-items:center;font-family:"Ubuntu",sans-serif;font-weight:700;color:#fff;border-radius:16px;height:30px}
.btn .pc{width:38px;height:38px;margin-left:-4px;margin-right:8px}
.btn-more{left:481px;top:128px;width:181px;background:linear-gradient(#ffcf2e,#f09c00);font-size:15px}
.divider{position:absolute;left:481px;top:176px;width:455px;height:5px;border-radius:3px;background:#fff;box-shadow:0 1px 2px rgba(0,0,0,.15)}
.quote{position:absolute;left:483px;top:197px;width:452px}
.quote h2{font-size:18px;font-weight:500;color:#111;margin-bottom:12px}
.quote h2 span{color:var(--red)}
.fields{display:flex;gap:8px;margin-bottom:10px}
.field{flex:1;height:28px;border:1px solid #c9d3dc;border-radius:4px;background:#fff;font-family:"Open Sans",sans-serif;font-size:12px;color:#888;padding:6px 9px}
.field-area{height:68px}
.btn-quote{left:776px;top:348px;width:158px;background:linear-gradient(#3fc0f2,#1a8fd0);font-size:16px}

.steps{position:absolute;left:0;top:465px;width:975px;height:59px;background:linear-gradient(#fafafa,#e7e9eb);border-top:1px solid #d3d6d9;border-bottom:1px solid #d3d6d9;display:flex;align-items:center;padding-left:38px;gap:8px}
.steps-icon{width:30px;height:34px}
.steps-title{font-size:14px;font-weight:500;margin-right:2px}
.steps-title b{font-weight:700}
.step{height:27px;line-height:25px;padding:0 8px;border-radius:14px;border:1px solid #d5d8db;background:#fff;font-weight:700;font-size:14px}
.step-1{color:var(--red)}
.step-2{color:var(--blue-dark)}
.step-3{color:var(--green-dark)}
.engines{position:absolute;left:0;top:524px;width:975px;height:58px;display:flex;align-items:center;justify-content:center;gap:7px;font-size:16px;color:#222}
.engine{font-weight:500;font-size:20px;color:#222}

.info{position:absolute;left:113px;top:678px;width:975px;height:290px;background:#fff}
.info-head{position:absolute;top:0;height:42px;display:flex;align-items:center;font-size:18px;font-weight:700;color:#fff;gap:10px;padding-left:16px}
.info-head .pc{width:30px;height:30px}
.head-why{left:0;width:622px;background:linear-gradient(90deg,#5fb826,#8fd13a 60%,#cfe8b4 92%,#bcd9ea)}
.head-say{left:622px;width:353px;background:linear-gradient(90deg,#7fbde0,#3a9fd8 30%,#2a8ed0)}
.why{position:absolute;left:18px;top:59px;width:580px;font-family:"Open Sans",sans-serif;font-size:10.4px;line-height:14px;color:#222}
.why p{margin-bottom:14px}
.why b{display:block;font-size:10.8px}
.say{position:absolute;left:632px;top:56px;width:326px;font-family:"Open Sans",sans-serif;font-size:10.3px;line-height:15px;color:#222}
.say blockquote{padding-bottom:14px;margin-bottom:14px;border-bottom:1px solid var(--line)}
.say cite{font-style:normal;color:var(--red)}
.btn-read{position:absolute;left:629px;top:235px;width:137px;height:24px;border-radius:12px;background:linear-gradient(#4cc4f2,#1f95d3);color:#fff;font-family:"Open Sans",sans-serif;font-size:10.5px;display:flex;align-items:center;gap:9px;padding-left:6px;white-space:nowrap}
.btn-read .pi{width:14px;height:14px}

.footer{position:absolute;left:0;top:974px;width:1200px;height:74px;background:var(--dark)}
.footer .brand{left:123px;top:14px}
.footer-links{position:absolute;left:701px;top:24px;font-family:"Open Sans",sans-serif;font-size:10.5px;line-height:15px;color:#a3a8ad;white-space:nowrap}
</style>
</head>
<body>

<header class="topbar">
  <div class="brand"><span class="brand-dot"></span>Clip Harbor Partners</div>
  <p class="tagline"><span class="hl-y">FIRST PAGE VIDEO LISTINGS</span> on Zentrova &amp; FlickBarn for the Keywords of Your Choice.<br>For More Traffic, Leads, and Sales to Your Site! <span class="hl-g">We Do It All For You.</span></p>
</header>

<main class="stage">
  <nav class="navbar">
    <ul class="nav">
      <li><a href="#" class="is-active"><svg class="pi" viewBox="0 0 16 16"><circle cx="8" cy="8" r="7" fill="none" stroke="#fff" stroke-width="2"/><path d="M6.5 5l4 3-4 3z" fill="#fff"/></svg>HOME</a></li>
      <li><a href="#"><svg class="pi" viewBox="0 0 16 16"><circle cx="8" cy="8" r="7" fill="none" stroke="#333" stroke-width="1.6"/><path d="M6.5 5l4 3-4 3z" fill="#333"/></svg>SERVICES</a></li>
      <li><a href="#"><svg class="pi" viewBox="0 0 16 16"><circle cx="8" cy="8" r="7" fill="none" stroke="#333" stroke-width="1.6"/><path d="M6.5 5l4 3-4 3z" fill="#333"/></svg>EXAMPLES</a></li>
      <li><a href="#"><svg class="pi" viewBox="0 0 16 16"><circle cx="8" cy="8" r="7" fill="none" stroke="#333" stroke-width="1.6"/><path d="M6.5 5l4 3-4 3z" fill="#333"/></svg>ORDER</a></li>
      <li><a href="#"><svg class="pi" viewBox="0 0 16 16"><circle cx="8" cy="8" r="7" fill="none" stroke="#333" stroke-width="1.6"/><path d="M6.5 5l4 3-4 3z" fill="#333"/></svg>CONTACT US</a></li>
    </ul>
    <div class="price">
      <svg class="price-icon" viewBox="0 0 62 52"><path d="M2 8h20l4 5h30v36H2z" fill="#cfd8df" stroke="#9aa6b0"/><rect x="32" y="18" width="26" height="32" fill="#2b2f33"/><g fill="#fff"><rect x="34" y="21" width="3" height="3"/><rect x="34" y="28" width="3" height="3"/><rect x="34" y="35" width="3" height="3"/><rect x="34" y="42" width="3" height="3"/><rect x="53" y="21" width="3" height="3"/><rect x="53" y="28" width="3" height="3"/><rect x="53" y="35" width="3" height="3"/><rect x="53" y="42" width="3" height="3"/></g><rect x="39" y="22" width="12" height="24" fill="#6e7a84"/></svg>
      <div class="price-label">STARTING AT<strong>$299*</strong></div>
    </div>
  </nav>

  <section class="hero">
    <div class="monitor">
      <svg width="422" height="316" viewBox="0 0 422 316" style="position:absolute;left:0;top:0"><rect x="0" y="0" width="422" height="272" rx="6" fill="#111"/><path d="M10 272h402l-40 12H50z" fill="#222"/><ellipse cx="211" cy="300" rx="70" ry="10" fill="#1a1a1a"/><rect x="150" y="284" width="122" height="14" fill="#0d0d0d"/></svg>
      <div class="screen" role="img" aria-label="Video player still: search results page with a smiling presenter standing on the right">
        <svg class="play-big" viewBox="0 0 60 64"><path d="M4 2l54 30L4 62z" fill="#fff" opacity=".85"/></svg>
        <div class="screen-copy">
          <div class="big">Video <span>SEO</span></div>
          <div class="think">think</div>
          <div class="small">THIS MIGHT BE <span>FOR YOU?</span></div>
        </div>
      </div>
    </div>

    <p class="hero-copy"><strong>VIDEO</strong> is Fast Becoming THE Preferred Method<br>to Expand Your TRAFFIC and SALES on the Internet for<br><span class="reasons">TWO Important Reasons...</span></p>
    <a href="#" class="btn btn-more"><svg class="pc" viewBox="0 0 38 38"><circle cx="19" cy="19" r="18" fill="#1c4f7a"/><circle cx="19" cy="19" r="13" fill="#fff"/><path d="M16 12l9 7-9 7z" fill="#1c4f7a"/></svg>FIND OUT MORE</a>
    <div class="divider"></div>

    <form class="quote">
      <h2>Get a <span>FREE</span> Quote</h2>
      <div class="fields"><div class="field">Name</div><div class="field">E-mail</div><div class="field">Phone No.</div></div>
      <div class="field field-area">Please tell us about your business goals, aspirations, challenges, etc.</div>
    </form>
    <a href="#" class="btn btn-quote"><svg class="pc" viewBox="0 0 38 38"><circle cx="19" cy="19" r="18" fill="#1c4f7a"/><circle cx="19" cy="19" r="13" fill="#fff"/><path d="M16 12l9 7-9 7z" fill="#1c4f7a"/></svg>GET A QUOTE</a>
  </section>

  <section class="steps">
    <svg class="steps-icon" viewBox="0 0 30 34"><rect x="4" y="2" width="24" height="28" fill="#cfd8df" stroke="#8e9aa4"/><rect x="1" y="8" width="24" height="25" fill="#2b2f33"/><path d="M9 14l9 6-9 6z" fill="#fff"/></svg>
    <span class="steps-title">START YOUR <b>VIDEOSEO STRATEGY</b> IN <b>3 EASY STEPS:</b></span>
    <span class="step step-1">01. CHOOSE PACKAGE</span>
    <span class="step step-2">02. FILL OUT FORM</span>
    <span class="step step-3">03. ENJOY THE TRAFFIC</span>
  </section>

  <section class="engines">
    Major Search Engines like <span class="engine">Zentrova</span>, <span class="engine">Vantiq</span>, <span class="engine">Orbelo</span> and <span class="engine">FlickBarn</span> are up to 53 times more likely to index a video.
  </section>
</main>

<section class="info">
  <h3 class="info-head head-why"><svg class="pc" viewBox="0 0 30 30"><circle cx="15" cy="15" r="14" fill="#2d7d14"/><circle cx="15" cy="15" r="10" fill="#7fcc35"/><path d="M12 9l8 6-8 6z" fill="#1f5c0c"/></svg>WHY CLIP HARBOR PARTNERS?</h3>
  <h3 class="info-head head-say"><svg class="pc" viewBox="0 0 30 30"><circle cx="15" cy="15" r="14" fill="#1c5f8c"/><circle cx="15" cy="15" r="10" fill="#46b0e8"/><path d="M12 9l8 6-8 6z" fill="#0f3e63"/></svg>WHAT PEOPLE SAY ABOUT US?</h3>

  <div class="why">
    <p>Lorem ipsum dolor sit amet, consectetur adipiscing elit. Donec vulputate imperdiet ullamcorper. Aenean ac sem lorem, porttitor cursus sem. Etiam vel erat purus, ac porta nisi. Curabitur at diam arcu. Nulla ac ante massa. Nulla eu ipsum tortor. Pellentesque in sagittis tortor.</p>
    <p><b>Maecenas dui felis, ullamcorper a sodales nec, mollis eu tellus.</b>Aenean vestibulum consequat est, quis tincidunt ante eleifend et. Cras accumsan metus velit, vel mattis risus. Donec blandit bibendum gravida. Vivamus pulvinar, nulla et vulputate faucibus, velit nisl sollicitudin sapien, a viverra nulla eros nec enim. Aenean at mauris in nibh facilisis aliquam. Nullam auctor suscipit egestas. Fusce libero tortor, semper id euismod et, pulvinar sed magna. Morbi imperdiet hendrerit porttitor.</p>
    <p><b>Praesent pretium tristique congue. Nullam scelerisque lacinia nisl a consectetur.</b>Donec vitae orci elit, non interdum mauris. Sed tortor metus, pellentesque ac rhoncus eget, suscipit a nisl. Pellentesque nec arcu risus, ac pulvinar sem. Suspendisse rutrum elementum libero, sit amet faucibus ante feugiat sit amet. Integer dignissim rhoncus ante, sed consectetur arcu accumsan in.</p>
  </div>

  <div class="say">
    <blockquote>"Exceeded our expectations by a mile. We not only have a picture video listing on the first page of Zentrova we also now occupy 6 out of 7 of the first places in Zentrova. […] just do it before they get too busy." <cite>- Daniel Ferris, wirestead.example</cite></blockquote>
    <blockquote>"Exceeded our expectations by a mile. We not only have a picture video listing on the first page of Zentrova we also now occupy 6 out of 7 of the first places in Zentrova. […] just do it before they get too busy." <cite>- Daniel Ferris, wirestead.example</cite></blockquote>
  </div>
  <a href="#" class="btn-read"><svg class="pi" viewBox="0 0 14 14"><circle cx="7" cy="7" r="7" fill="#fff" opacity=".5"/><path d="M5.5 4l4 3-4 3z" fill="#fff"/></svg>read all Testimonials</a>
</section>

<footer class="footer">
  <div class="brand"><span class="brand-dot"></span>Clip Harbor Partners</div>
  <div class="footer-links">Home . Services . Examples . Order . Contact us . Terms of Use . Privacy Policy<br>© 2011 Clip Harbor Partners.&nbsp; All rights reserved.</div>
</footer>

</body>
</html>
```